IT Company looking to market towards Dental Offices

I am looking for a full-color design. Using my existing logo. Must have High Res stock photos. The brochure needs to be full page edge to edge design single fold pamphlet style. Content provided. Please see the website in attached Word Doc for more content.

```html
<!DOCTYPE html>
<html lang="en">
<head>
<meta charset="utf-8">
<title>Byte Harbor – Dental Technology Services</title>
<link href="https://fonts.googleapis.com/css2?family=Open+Sans:wght@400;600&display=swap" rel="stylesheet">
<style>
  :root {
    --accent: #c55a11;
    --ink: #2e2e2e;
    --navy: #1f3864;
    --paper: #ffffff;
    --bg-light: #eceaea;
    --bg-mid: #d4d5d9;
    --bg-dark: #b9bcc4;
  }
  * { margin: 0; padding: 0; box-sizing: border-box; }
  html, body { width: 831px; height: 1200px; overflow: hidden; }
  body { font-family: "Open Sans", Arial, sans-serif; color: var(--ink); }
  .brochure {
    position: relative; width: 831px; height: 1200px; overflow: hidden;
    background: var(--paper);
  }
  .backdrop {
    position: absolute; left: 0; top: 0; width: 831px; height: 1146px;
    background:
      radial-gradient(ellipse at 78% 12%, rgba(255,255,255,0.5), transparent 55%),
      linear-gradient(160deg, var(--bg-light) 0%, #e2e1e3 35%, var(--bg-mid) 65%, var(--bg-dark) 100%);
  }
  .intro { position: absolute; left: 27px; top: 58px; width: 390px; font-size: 19.5px; line-height: 28px; }
  .intro p + p { margin-top: 12px; }
  .intro .lead { color: var(--accent); font-size: 40px; line-height: 40px; }
  .cta { position: absolute; left: 27px; top: 372px; width: 400px; }
  .cta h2 { font-weight: 400; font-size: 26.5px; line-height: 36px; letter-spacing: 0.3px; }
  .cta h2 span, .section h2 span { color: var(--accent); }
  .cta .sub { margin-top: 18px; font-size: 19px; line-height: 27px; }
  .steps { list-style: none; margin-top: 14px; font-size: 19px; line-height: 27.5px; }
  .steps li { display: flex; margin-bottom: 0; }
  .steps li b { font-weight: 400; width: 40px; flex: none; }
  .network-photo { position: absolute; left: 34px; top: 765px; }
  .section { position: absolute; left: 481px; width: 340px; }
  .section h2 { font-weight: 400; font-size: 25px; color: var(--accent); letter-spacing: 0.5px; line-height: 30px; }
  .section ul { list-style: none; margin-top: 8px; font-size: 18.5px; line-height: 26px; }
  .section li { position: relative; padding-left: 42px; }
  .section li::before { content: "•"; position: absolute; left: 23px; }
  .hardware { top: 72px; }
  .solutions { top: 369px; }
  .infrastructure { top: 790px; }
  .footer {
    position: absolute; left: 0; top: 1146px; width: 831px; height: 54px;
    background: var(--paper); color: var(--navy);
    font-size: 23.5px; text-align: center; line-height: 54px; letter-spacing: 0.3px;
  }
</style>
</head>
<body>
<main class="brochure">
  <div class="backdrop" role="img" aria-label="Soft-focus photo of a laptop keyboard with code on the screen"></div>

  <section class="intro">
    <p><span class="lead">Don’t</span> let Technology Departments, Hardware Vendors and Practice Management vendors Point Fingers at each other.</p>
    <p>We collaborate everything and everyone for you, make one call to us and let us handle your technology.</p>
  </section>

  <section class="cta">
    <h2><span>READY</span> TO MAKE YOUR<br>TECHNOLOGY WORK?</h2>
    <p class="sub">How To Achieve Technology Bliss for Your Practice</p>
    <ol class="steps">
      <li><b>1.</b><span>Schedule a FREE Network &amp; Technology Evaluation</span></li>
      <li><b>2.</b><span>Receive your Flat Rate Price and Technology Quote</span></li>
      <li><b>3.</b><span>Sit back and let Byte Harbor take care of everything.</span></li>
    </ol>
  </section>

  <svg class="network-photo" width="404" height="258" viewBox="0 0 404 258" role="img" aria-label="Photo of a network switch with patched blue, yellow and red ethernet cables">
    <defs>
      <linearGradient id="cableTones" x1="0" y1="0" x2="1" y2="1">
        <stop offset="0" stop-color="#3b5fa8"/>
        <stop offset="0.45" stop-color="#4a6fb8"/>
        <stop offset="0.75" stop-color="#3a3c44"/>
        <stop offset="1" stop-color="#1e1f24"/>
      </linearGradient>
    </defs>
    <polygon points="2,20 402,2 402,172 214,256 2,172" fill="url(#cableTones)"/>
  </svg>

  <section class="section hardware">
    <h2>HARDWARE SALES</h2>
    <ul>
      <li>Servers</li><li>Workstations</li><li>Firewalls</li><li>Routers</li>
      <li>Switches</li><li>TVs &amp; Monitors</li><li>Wireless Equipment</li>
      <li>Custom Check-in Workstations</li>
    </ul>
  </section>

  <section class="section solutions">
    <h2>SOLUTIONS</h2>
    <ul>
      <li>Flat Rate Monthly Support</li>
      <li>Secure Backups with our ToothSafeVault.net</li>
      <li>Secure Encrypted Emails &amp; X-Rays</li>
      <li>Practice Management Software Experts</li>
      <li>HIPAA Compliance</li>
      <li>Anti-Virus, Anti-Malware and Cyber Security</li>
      <li>Data Recovery</li>
      <li>Cloud Office / Mail Suites</li>
      <li>Phone VOIP &amp; SIP Trunks</li>
    </ul>
  </section>

  <section class="section infrastructure">
    <h2>INFRASTRUCTURE</h2>
    <ul>
      <li>Data &amp; Voice Cable</li>
      <li>HDMI &amp; COAX Video Cable</li>
      <li>TV &amp; Dual Monitor Installation</li>
      <li>Mounting Hardware</li>
      <li>Wireless Installation</li>
      <li>Office Sound Solutions</li>
      <li>Custom Dental Cable</li>
      <li>Video Surveillance</li>
    </ul>
  </section>

  <footer class="footer">48 W. Maple Grove&nbsp; Fairview, KS 66012&nbsp;&nbsp; - &nbsp;&nbsp;555.204.7718</footer>
</main>
</body>
</html>
```